Design Business Cards for my forest, wood company

Hi ,
I need that you create Business Card and for my forest, wood company
display on it Name Surname , job position(Director) , the type of work we do (logging ,woodworking) ,
telephone number , email ,
and our adress with bank account which is written togehter in 4 rows
example for adress and bank account it has to be together ,
Reg.Nr. 871290536
Milteva Gorsin Ti
Peldura Viskot LE-5817
KVT LE71QOVR0004817562

Suggested colors are Green , yellow , black , brown

also you need to add,create nice looking and simple logo with my bussines name which has some kind of icon or symbol, picture . I add logo example what I want in it , three icons in one there is trees , in other there is wood planks and in third ear field .
My company name "GRĒVULU TOMIŅAS"

I add my bussines name in picture format , because it includes signs which are not in english.
I add Business card example which I like , it has everything I mentioned .

If any question please ask , if I will see business card which I like will award it immediately .

```html
<!DOCTYPE html>
<html lang="en">
<head>
<meta charset="utf-8">
<title>Grēvulu Tomiņas – Business Card</title>
<link href="https://fonts.googleapis.com/css2?family=Didact+Gothic&family=Crimson+Text:wght@400;600&display=swap" rel="stylesheet">
<style>
  :root {
    --page: #e8e5e0;
    --forest: #36433a;
    --bark: #6e4519;
    --bark-dark: #3a1f12;
    --leaf: #5fae47;
    --logo-mark: #79b84a;
    --cream: #efe3c8;
    --mist: #e2e2dc;
    --white: #ffffff;
  }
  * { box-sizing: border-box; margin: 0; padding: 0; }
  html, body { width: 1200px; height: 856px; overflow: hidden; }
  body {
    background: var(--page);
    display: flex;
    flex-direction: column;
    align-items: center;
    justify-content: center;
    gap: 44px;
    font-family: "Didact Gothic", sans-serif;
  }
  .card {
    position: relative;
    width: 640px;
    height: 366px;
    border-radius: 24px;
    overflow: hidden;
    background: var(--forest);
    box-shadow: 0 6px 18px rgba(0,0,0,0.18);
  }
  .card-shapes { position: absolute; inset: 0; }

  .brand { position: absolute; display: flex; align-items: center; }
  .brand-mark {
    background: var(--logo-mark);
    border-radius: 6px;
    flex: none;
  }
  .brand-name {
    color: var(--leaf);
    font-family: "Didact Gothic", sans-serif;
    letter-spacing: 1px;
  }

  /* Front */
  .card-front .brand { left: 118px; top: 128px; gap: 20px; }
  .card-front .brand-mark { width: 66px; height: 66px; }
  .card-front .brand-name { font-size: 27px; }
  .tagline {
    position: absolute;
    left: 204px;
    top: 210px;
    color: var(--mist);
    font-size: 21px;
    letter-spacing: 0.5px;
    padding-bottom: 8px;
    border-bottom: 1px solid rgba(226,226,220,0.6);
  }

  /* Back */
  .card-back .brand { left: 34px; top: 34px; gap: 14px; }
  .card-back .brand-mark { width: 56px; height: 56px; }
  .card-back .brand-name { font-size: 20px; }
  .person {
    position: absolute;
    right: 70px;
    top: 84px;
    text-align: center;
    color: var(--white);
    font-family: "Crimson Text", serif;
    line-height: 1;
  }
  .person-name { font-size: 26px; font-weight: 600; }
  .person-role { font-size: 17px; margin-top: 2px; }
  .address {
    position: absolute;
    left: 40px;
    top: 196px;
    color: var(--cream);
    font-family: "Crimson Text", serif;
    font-size: 18px;
    line-height: 25px;
  }
  .contacts {
    position: absolute;
    left: 388px;
    top: 184px;
    list-style: none;
    color: var(--white);
    font-family: "Crimson Text", serif;
    font-size: 17px;
    line-height: 24px;
  }
  .contacts li { display: flex; align-items: center; gap: 10px; }
  .contact-icon { width: 16px; height: 16px; flex: none; }
</style>
</head>
<body>

<section class="card card-front">
  <svg class="card-shapes" viewBox="0 0 640 366" width="640" height="366" aria-hidden="true">
    <polygon points="0,0 260,0 0,62" fill="var(--bark-dark)"/>
    <polygon points="260,0 640,0 640,16 0,92 0,62" fill="var(--bark)"/>
    <polygon points="0,344 640,268 640,300 0,366" fill="var(--bark)"/>
    <polygon points="640,300 640,366 420,366" fill="var(--bark-dark)"/>
  </svg>
  <div class="brand">
    <span class="brand-mark"></span>
    <span class="brand-name">GRĒVULU TOMIŅAS</span>
  </div>
  <p class="tagline">Logging &amp; Wood Working</p>
</section>

<section class="card card-back">
  <svg class="card-shapes" viewBox="0 0 640 366" width="640" height="366" aria-hidden="true">
    <rect x="0" y="158" width="640" height="208" fill="var(--bark)"/>
    <line x1="0" y1="158" x2="640" y2="158" stroke="var(--white)" stroke-width="1.5" stroke-dasharray="5 4"/>
  </svg>
  <div class="brand">
    <span class="brand-mark"></span>
    <span class="brand-name">GRĒVULU TOMIŅAS</span>
  </div>
  <div class="person">
    <p class="person-name">Name</p>
    <p class="person-role">Director</p>
  </div>
  <address class="address" style="font-style:normal">
    Reg.Nr. 871290536<br>
    Milteva Gorsin Ti<br>
    Peldura Viskot LE-5817<br>
    KVT LE71QOVR0004817562
  </address>
  <ul class="contacts">
    <li>
      <svg class="contact-icon" viewBox="0 0 16 16"><rect x="0.5" y="0.5" width="15" height="15" rx="3" fill="var(--white)"/><path d="M5 3.5 L7 5.5 L6 7 Q7 9 9 10 L10.5 9 L12.5 11 L11 12.5 Q7 12.5 3.5 5 Z" fill="var(--bark)"/></svg>
      <span>9386 2275</span>
    </li>
    <li>
      <svg class="contact-icon" viewBox="0 0 16 16"><rect x="0.5" y="0.5" width="15" height="15" rx="3" fill="var(--white)"/><rect x="3" y="5" width="10" height="7" fill="none" stroke="var(--bark)" stroke-width="1.2"/><path d="M3 5 L8 9 L13 5" fill="none" stroke="var(--bark)" stroke-width="1.2"/></svg>
      <span>info@mailbox.com.au</span>
    </li>
    <li>
      <svg class="contact-icon" viewBox="0 0 16 16"><circle cx="8" cy="8" r="7.5" fill="var(--white)"/><circle cx="8" cy="8" r="5" fill="none" stroke="var(--bark)" stroke-width="1.1"/><ellipse cx="8" cy="8" rx="2" ry="5" fill="none" stroke="var(--bark)" stroke-width="1.1"/><line x1="3" y1="8" x2="13" y2="8" stroke="var(--bark)" stroke-width="1.1"/></svg>
      <span>www.timberandlog.com</span>
    </li>
  </ul>
</section>

</body>
</html>
```